Debut book club fiction author needs a book cover design

I need a book cover design (and a separate e-book thumbnail also) for my book club/women's fiction debut that I am launching on Brightleaf Press Portal. I've included the brief/back cover blurb as below to give you a flavour of the book. I'm after something striking but simple, maybe with a wine glass lurking in the background and/or an abandoned dummy/pacifier or empty crib?? I've attached a few competitor style covers that i like for reference.

Target Market(s)

Women's fiction readers

Industry/Entity Type

Women's fiction/publishing

Font styles to use
Serif

Requirements
Must have
• Title: Every Quiet Hour. Name: Maren Tolley. The full 'pitch/blurb' on the back cover which I've included as a file below named 'pitch'
Nice to have
• Open to suggestions, but an image which reflects the struggle captured in the book in a bold simple image

```html
<!DOCTYPE html>
<html lang="en">
<head>
<meta charset="utf-8">
<title>Every Quiet Hour – Full Wrap Cover</title>
<link rel="stylesheet" href="https://fonts.googleapis.com/css2?family=Bebas+Neue&family=Great+Vibes&family=Lato:wght@400;700&family=Mulish:wght@400&display=swap">
<style>
  :root {
    --backdrop: #b1afb0;
    --paper: #ffffff;
    --rose: #ee4580;
    --charcoal: #3f4043;
    --ink: #1f1f1f;
    --bubble: #e6e6e7;
    --guide: #3b3bff;
    --note: #8e8c8d;
  }
  * { margin: 0; padding: 0; box-sizing: border-box; }
  html, body {
    width: 715px;
    height: 1200px;
    overflow: hidden;
    background: var(--backdrop);
  }
  .wrap-cover {
    position: absolute;
    left: 20px;
    top: 385px;
    width: 675px;
    height: 429px;
    background: var(--paper);
  }
  .spine-guide {
    position: absolute;
    top: -28px;
    height: 485px;
    border-left: 1px dashed var(--guide);
  }
  .spine-guide--left { left: 324px; }
  .spine-guide--right { left: 350px; }

  /* Back cover */
  .back-cover {
    position: absolute;
    left: 0; top: 0;
    width: 324px; height: 429px;
  }
  .tagline {
    position: absolute;
    left: 40px; top: 36px;
    width: 240px;
    text-align: center;
    font-family: "Great Vibes", cursive;
    color: var(--rose);
    font-size: 19px;
    line-height: 21px;
  }
  .blurb {
    position: absolute;
    left: 48px; top: 94px;
    width: 226px;
    text-align: center;
    font-family: "Lato", sans-serif;
    font-size: 6.6px;
    line-height: 9.2px;
    color: var(--ink);
  }
  .author-portrait {
    position: absolute;
    left: 32px; top: 264px;
    width: 100px; height: 110px;
    border-radius: 45px 45px 8px 8px;
    background: #000;
  }
  .about-author {
    position: absolute;
    left: 91px; top: 284px;
    width: 202px; height: 71px;
    border-radius: 16px;
    background: var(--bubble);
    padding: 10px 12px 0 42px;
    font-family: "Lato", sans-serif;
    color: var(--ink);
  }
  .about-author h3 {
    font-size: 7px;
    font-weight: 700;
    margin-bottom: 1px;
  }
  .about-author p {
    font-size: 5.9px;
    line-height: 9px;
  }
  .author-portrait { z-index: 2; }
  .trim-note {
    position: absolute;
    left: 10px; top: 432px;
    font-family: "Lato", sans-serif;
    font-size: 4.8px;
    line-height: 6px;
    color: var(--note);
    white-space: pre;
  }

  /* Spine */
  .spine {
    position: absolute;
    left: 324px; top: 0;
    width: 26px; height: 429px;
  }
  .spine-author, .spine-title {
    position: absolute;
    left: 13px;
    transform: translate(-50%, -50%) rotate(-90deg);
    white-space: nowrap;
  }
  .spine-author {
    top: 78px;
    font-family: "Mulish", sans-serif;
    font-size: 15px;
    color: var(--ink);
  }
  .spine-title {
    top: 327px;
    display: flex;
    align-items: baseline;
    gap: 3px;
  }
  .spine-title .script {
    font-family: "Great Vibes", cursive;
    font-size: 18px;
    color: var(--rose);
  }
  .spine-title .bold {
    font-family: "Bebas Neue", sans-serif;
    font-size: 19px;
    color: var(--rose);
  }
  .spine-title .bold--dark { color: var(--charcoal); }

  /* Front cover */
  .front-cover {
    position: absolute;
    left: 350px; top: 0;
    width: 325px; height: 429px;
  }
  .title {
    position: absolute;
    left: 0; top: 22px;
    width: 325px;
    text-align: center;
  }
  .title-script {
    display: block;
    font-family: "Great Vibes", cursive;
    font-size: 40px;
    line-height: 36px;
    color: var(--rose);
  }
  .title-line {
    display: block;
    font-family: "Bebas Neue", sans-serif;
    font-size: 76px;
    line-height: 60px;
    letter-spacing: -1px;
  }
  .title-line--rose { color: var(--rose); }
  .title-line--dark { color: var(--charcoal); }
  .cover-image {
    position: absolute;
    left: 16px; top: 191px;
    width: 280px; height: 172px;
    background: radial-gradient(ellipse 55% 50% at 58% 45%, #f1a38e 0%, #f6c9b8 45%, #fbeee9 75%, var(--paper) 100%);
  }
  .front-author {
    position: absolute;
    left: 0; top: 370px;
    width: 325px;
    text-align: center;
    font-family: "Mulish", sans-serif;
    font-size: 24px;
    color: var(--ink);
  }
</style>
</head>
<body>
  <main class="wrap-cover">
    <section class="back-cover">
      <p class="tagline">All the women wanted was a child of their own...’</p>
      <p class="blurb">
        Reception teacher, Lana, and partner and part-time DJ Joel can’t afford private IVF treatment. Equally they can’t afford not to. Lana’s mental health is deteriorating as she longs for the child that has eluded her to date.<br>
        In her 37 years Tilda Asquith-Hyde has never felt maternal. However, following the breakdown of her long-term relationship, and mother’s death she finds herself in receipt of an eye-watering inheritance. No longer needing to work she becomes increasingly isolated and even alcohol, her only constant, no longer fills the void. After a chance encounter with an old friend and her baby, Tilda seizes upon the idea that motherhood will be the missing piece in her lonely life.<br>
        Both parties access IVF treatment at the same clinic, Tilda opting for a sperm donor and Lana and Joel using their own fertilised egg.<br>
        But within moments of giving birth, Tilda is convinced that the child in her arms is not biologically hers, setting off a devastating chain of events. How far will both women go to ‘do the right thing’ for their children? It’s enough to drive anyone to drink. Isn’t it?
      </p>
      <div class="author-portrait" role="img" aria-label="Silhouette portrait of the author"></div>
      <div class="about-author">
        <h3>About the Author</h3>
        <p>Lorem ipsum dolor sit amet, consectetuer adipiscing elit, sed diam nonummy nibh euismod tincidunt ut laoreet dolore magna aliquam erat volutpat. Ut wisi enim ad minim</p>
      </div>
      <p class="trim-note">Back Cover
8.25" x 11"      (209.55mm x 279.40mm)</p>
    </section>

    <section class="spine">
      <span class="spine-author">Maren Tolley</span>
      <span class="spine-title">
        <span class="script">Every</span>
        <span class="bold">QUIET</span>
        <span class="bold bold--dark">HOUR</span>
      </span>
    </section>

    <section class="front-cover">
      <h1 class="title">
        <span class="title-script">Every</span>
        <span class="title-line title-line--rose">QUIET</span>
        <span class="title-line title-line--dark">HOUR</span>
      </h1>
      <div class="cover-image" role="img" aria-label="Soft photograph of a newborn's tiny hand gripping an adult's fingers on white blanket"></div>
      <p class="front-author">Maren Tolley</p>
    </section>

    <div class="spine-guide spine-guide--left"></div>
    <div class="spine-guide spine-guide--right"></div>
  </main>
</body>
</html>
```